Delivery Performance Dashboard for Web Portal

We need you to design a dashboard for our web portal. We deliver sand and stone to construction jobsites. The attached screenshot is from our current web portal dashboard . It shows how much material has been delivered from an order.

Dump trucks will deliver multiple loads during the day and the dispatcher uses the dashboard to monitor if they need to add more trucks or less trucks to fulfill the order. An example would be, I need to ship 1,000 tons of sand to a jobsite and I plan to use 10 trucks during the day and that it will take 10 hours of hauling to complete the job. After 5 hours of hauling (50% the day is over), I should have delivered 500 tons of sand (50% of the order). But maybe there is a lot of traffic, and I only have delivered 300 tons. The dashboard will show that I am behind schedule and I might need to add 2 more trucks to the job.

Industry/Entity Type

Construction

Font styles to use
Sans Serif

Requirements
Must have
• We need a progress bar showing how much material has been delivered, how much material was requested to be delivered total and how much material should have been delivered at the current time. The goal is to show the user if the deliveries are ahead or behind the expected pace and why.
Nice to have
• The icons for plant, driving and jobsite show if the actual times have exceeded or beaten the planned times. Maybe you have other ideas to show the user if the trucks are sitting longer on the jobsite, at the plant to get loaded or driving to and from the jobsite.

```html
<!DOCTYPE html>
<html lang="en">
<head>
<meta charset="utf-8">
<title>Delivery Performance Dashboard</title>
<link href="https://fonts.googleapis.com/css2?family=Poppins:wght@300;400;500;600&display=swap" rel="stylesheet">
<style>
:root{
  --bg:#eef4fd;
  --white:#ffffff;
  --ink:#2f3440;
  --muted:#8a8f99;
  --nav-label:#8fa6d8;
  --head-a:#7b5ccd;
  --head-b:#5a8be0;
  --table-head:#5b7fdb;
  --line:#e6e9ef;
  --bar:#6275dc;
  --blue:#1479ee;
  --red:#e13a4b;
  --yellow:#f6c000;
  --green:#23a646;
  --teal:#17a2b8;
  --plus:#1e9a3c;
}
*{box-sizing:border-box;margin:0;padding:0}
html,body{width:1200px;height:551px;overflow:hidden}
body{font-family:'Poppins',sans-serif;background:var(--bg);color:var(--ink);position:relative}
.topbar{position:absolute;left:0;top:0;width:1200px;height:35px;background:linear-gradient(90deg,var(--head-a),var(--head-b));color:var(--white)}
.brand{position:absolute;left:11px;top:5px;font-size:15px;font-weight:600}
.menu-btn{position:absolute;left:120px;top:7px;width:19px;height:19px;background:var(--white);border-radius:3px}
.top-link{position:absolute;top:11px;font-size:9px}
.search{position:absolute;left:911px;top:6px;width:138px;height:22px;background:var(--white);border-radius:2px;font-size:8px;color:#b5b9c2;padding:6px 0 0 23px}
.search svg{position:absolute;left:7px;top:6px}
.top-icon{position:absolute;top:10px}
.badge{position:absolute;left:1108px;top:8px;width:8px;height:8px;border-radius:50%;background:var(--red);font-size:6px;text-align:center;line-height:8px}
.top-avatar{position:absolute;left:1129px;top:4px;width:28px;height:28px;border-radius:50%;background:linear-gradient(135deg,#c98a62,#7a4a30);border:2px solid var(--white)}
.sidebar{position:absolute;left:0;top:35px;width:159px;height:516px;background:var(--white);border-right:1px solid var(--line)}
.profile{height:56px;background:#f7f8fa;border-bottom:1px solid var(--line);position:relative}
.avatar{position:absolute;left:10px;top:9px;width:36px;height:36px;border-radius:50%;background:linear-gradient(135deg,#d29a73,#6e4029)}
.profile-name{position:absolute;left:54px;top:15px;font-size:10px;font-weight:500}
.profile-mail{position:absolute;left:54px;top:28px;font-size:7.5px}
.nav-label{position:absolute;left:12px;font-size:6.5px;color:var(--nav-label)}
.nav-item{position:absolute;left:14px;width:132px;font-size:9px;display:flex;align-items:center;gap:9px}
.nav-item .chev{margin-left:auto}
.divider{position:absolute;left:0;width:159px;border-top:1px solid var(--line)}
.slogan{position:absolute;left:179px;top:61px;font-size:16px;font-weight:500}
.orders{position:absolute;left:174px;top:101px;width:1019px;height:288px;background:var(--white)}
.orders-head{height:44px;background:var(--table-head);color:var(--white);position:relative;font-size:9.5px}
.orders-head span{position:absolute;top:15px;display:flex;align-items:center;gap:6px}
.sort{font-size:6px;line-height:7px;display:inline-block;text-align:center;font-style:normal}
.row{position:relative;height:54px;border-bottom:1px solid var(--line);font-size:8.5px}
.row:last-child{border-bottom:none}
.cell{position:absolute;top:22px;white-space:nowrap}
.tons{position:absolute;left:601px;top:19px;width:163px}
.tons .track{height:5px;background:var(--bar);border-radius:3px}
.tons .meta{display:flex;justify-content:space-between;font-size:7.5px;margin-top:7px}
.waits{position:absolute;left:785px;top:23px;display:flex;gap:6px;align-items:center}
.plus{color:var(--plus)}
.minus{color:var(--red)}
.card{position:absolute;top:401px;width:250px;height:131px;background:var(--white)}
.card-close{position:absolute;right:14px;top:10px;font-size:9px}
.card-title{position:absolute;left:13px;top:10px;font-size:12.5px}
.card-sub{position:absolute;left:13px;top:29px;font-size:7.5px;color:var(--muted)}
.card-kind{position:absolute;left:10px;top:52px;font-size:9.5px;color:#555a64;display:flex;align-items:center;gap:6px}
.metric{position:absolute;left:10px;height:12px;width:230px;font-size:8.5px;color:#666b75}
.metric .lbl{position:absolute;left:0;top:0;width:37px;text-align:right;white-space:nowrap;line-height:12px}
.metric .bar{position:absolute;left:42px;top:4px;height:5px;border-radius:3px}
.metric .val{position:absolute;top:-3px;line-height:12px}
</style>
</head>
<body>
<header class="topbar">
  <div class="brand">Your Logo</div>
  <div class="menu-btn"><svg width="19" height="19"><g stroke="#7a6fd3" stroke-width="1.2"><line x1="5" y1="6" x2="14" y2="6"/><line x1="5" y1="9" x2="14" y2="9"/><line x1="5" y1="12" x2="11" y2="12"/></g></svg></div>
  <div class="top-link" style="left:161px">Dropdown ⌄</div>
  <div class="top-link" style="left:235px">More Links ⌄</div>
  <div class="search"><svg width="10" height="10"><circle cx="4" cy="4" r="3" fill="none" stroke="#777" stroke-width="1.2"/><line x1="6.5" y1="6.5" x2="9" y2="9" stroke="#777" stroke-width="1.2"/></svg>Search...</div>
  <svg class="top-icon" style="left:1061px" width="14" height="13"><path d="M1 1h12v8H6l-3 3V9H1z" fill="none" stroke="#fff" stroke-width="1.3"/></svg>
  <svg class="top-icon" style="left:1093px" width="13" height="14"><path d="M6.5 1a4 4 0 0 1 4 4v4l1.5 2H1l1.5-2V5a4 4 0 0 1 4-4z" fill="none" stroke="#fff" stroke-width="1.3"/><circle cx="6.5" cy="12.5" r="1.3" fill="#fff"/></svg>
  <div class="badge">2</div>
  <div class="top-avatar" role="img" aria-label="User profile photo"></div>
  <svg class="top-icon" style="left:1168px;top:12px" width="12" height="11"><g stroke="#fff" stroke-width="1.3"><line x1="0" y1="1" x2="12" y2="1"/><line x1="3" y1="5" x2="12" y2="5"/><line x1="0" y1="9" x2="12" y2="9"/></g></svg>
</header>

<aside class="sidebar">
  <div class="profile">
    <div class="avatar" role="img" aria-label="User profile photo"></div>
    <div class="profile-name">Dana Holt</div>
    <div class="profile-mail">hello@gravelworks.io</div>
  </div>
  <div class="nav-label" style="top:82px">NAVIGATION</div>
  <div class="nav-item" style="top:98px"><svg width="11" height="8"><path d="M1 7a4.5 4.5 0 0 1 9 0" fill="none" stroke="#444" stroke-width="1.2"/><line x1="5.5" y1="7" x2="8" y2="3" stroke="#444" stroke-width="1.2"/></svg>Dashboards<span class="chev">⌄</span></div>
  <div class="divider" style="top:129px"></div>
  <div class="nav-label" style="top:143px">SUB MENU</div>
  <div class="nav-item" style="top:160px"><svg width="11" height="10"><rect x="1" y="1" width="9" height="6" fill="none" stroke="#444"/><line x1="3" y1="9" x2="8" y2="9" stroke="#444"/></svg>Menu Item<span class="chev">⌄</span></div>
  <div class="nav-item" style="top:185px"><svg width="11" height="11"><path d="M5.5 1l1.3 3h3l-2.4 2 1 3.2-2.9-1.9-2.9 1.9 1-3.2L1.2 4h3z" fill="none" stroke="#444" stroke-width=".9"/></svg>Menu Item<span class="chev">⌄</span></div>
  <div class="divider" style="top:216px"></div>
  <div class="nav-label" style="top:229px">SUB MENU</div>
  <div class="nav-item" style="top:245px"><svg width="11" height="11"><circle cx="5.5" cy="5.5" r="4.5" fill="none" stroke="#444"/><line x1="5.5" y1="4.5" x2="5.5" y2="8" stroke="#444"/><circle cx="5.5" cy="3" r=".7" fill="#444"/></svg>Menu Item</div>
  <div class="nav-item" style="top:270px"><svg width="11" height="11"><circle cx="5.5" cy="5.5" r="2" fill="none" stroke="#444"/><circle cx="5.5" cy="5.5" r="4.2" fill="none" stroke="#444" stroke-dasharray="2 1.3"/></svg>Menu Item</div>
  <div class="divider" style="top:301px"></div>
  <div class="nav-label" style="top:314px">SUB MENU</div>
  <div class="nav-item" style="top:328px"><svg width="11" height="10"><rect x="1" y="1" width="9" height="8" fill="none" stroke="#444"/><line x1="1" y1="4" x2="10" y2="4" stroke="#444"/><line x1="5.5" y1="4" x2="5.5" y2="9" stroke="#444"/></svg>Menu Item</div>
  <div class="nav-item" style="top:354px"><svg width="11" height="11"><path d="M6 1l4 4-2 1-2 2 0 2-5-5 2 0 2-2z M3 8l-2 2" fill="none" stroke="#444" stroke-width=".9"/></svg>Menu Item</div>
  <div class="divider" style="top:385px"></div>
</aside>

<h1 class="slogan">Header Slogan Goes Here</h1>

<section class="orders">
  <div class="orders-head">
    <span style="left:8px">Order <i class="sort">⌃<br>⌄</i></span>
    <span style="left:85px">Origin <i class="sort">⌃<br>⌄</i></span>
    <span style="left:221px">Destination <i class="sort">⌃<br>⌄</i></span>
    <span style="left:361px">Customer <i class="sort">⌃<br>⌄</i></span>
    <span style="left:536px">Status <i class="sort">⌃<br>⌄</i></span>
    <span style="left:602px">Tons <i class="sort" style="margin-left:24px">⌃<br>⌄</i></span>
    <span style="left:786px">Wait Times <i class="sort">⌃<br>⌄</i></span>
    <span style="left:891px">Remaining <i class="sort">⌃<br>⌄</i></span>
    <span style="left:976px">+ / − <svg width="10" height="8"><rect x="0" y="1" width="6" height="5" fill="#fff"/><path d="M6 3h2.5l1.5 2v1H6z" fill="#fff"/><circle cx="2" cy="7" r="1" fill="#fff"/><circle cx="8" cy="7" r="1" fill="#fff"/></svg></span>
  </div>
  <div class="rows">
    <div class="row">
      <span class="cell" style="left:20px">177746</span>
      <span class="cell" style="left:83px">Cedar Ridge Asphalt Plant</span>
      <span class="cell" style="left:218px">BZJV-185 from mm 77-98</span>
      <span class="cell" style="left:358px">Harlow Construction - North Division</span>
      <span class="cell" style="left:535px">Accepted</span>
      <div class="tons"><div class="track"></div><div class="meta"><span>722.57 / 1500</span><span>7:30 am - 5:00 pm</span></div></div>
      <div class="waits">
        <svg width="18" height="8"><path d="M0 8V2l3 2V2l3 2V0h2v8z" fill="#666"/><path d="M13 3l2.5 3h-5z" fill="var(--red)"/></svg>
        <svg width="22" height="8"><rect x="0" y="1" width="6" height="5" fill="#666"/><path d="M6 2.5h2.5l1.5 2V6H6z" fill="#666"/><circle cx="2" cy="7" r="1" fill="#666"/><circle cx="8" cy="7" r="1" fill="#666"/><path d="M17 3l2.5 3h-5z" fill="var(--red)"/></svg>
        <svg width="18" height="9"><path d="M3.5 0a3 3 0 0 1 3 3c0 2-3 6-3 6s-3-4-3-6a3 3 0 0 1 3-3z" fill="#666"/><circle cx="3.5" cy="3" r="1" fill="#fff"/><path d="M11 3h5l-2.5 3z" fill="var(--green)"/></svg>
      </div>
      <span class="cell plus" style="left:891px">+1:25 hrs</span>
      <span class="cell minus" style="left:975px">-31</span>
    </div>
    <div class="row">
      <span class="cell" style="left:20px">177746</span>
      <span class="cell" style="left:83px">Cedar Ridge Asphalt Plant</span>
      <span class="cell" style="left:218px">BZJV-185 from mm 77-98</span>
      <span class="cell" style="left:358px">Harlow Construction - North Division</span>
      <span class="cell" style="left:535px">Accepted</span>
      <div class="tons"><div class="track"></div><div class="meta"><span>722.57 / 1500</span><span>7:30 am - 5:00 pm</span></div></div>
      <div class="waits">
        <svg width="18" height="8"><path d="M0 8V2l3 2V2l3 2V0h2v8z" fill="#666"/><path d="M13 3l2.5 3h-5z" fill="var(--red)"/></svg>
        <svg width="22" height="8"><rect x="0" y="1" width="6" height="5" fill="#666"/><path d="M6 2.5h2.5l1.5 2V6H6z" fill="#666"/><circle cx="2" cy="7" r="1" fill="#666"/><circle cx="8" cy="7" r="1" fill="#666"/><path d="M17 3l2.5 3h-5z" fill="var(--red)"/></svg>
        <svg width="18" height="9"><path d="M3.5 0a3 3 0 0 1 3 3c0 2-3 6-3 6s-3-4-3-6a3 3 0 0 1 3-3z" fill="#666"/><circle cx="3.5" cy="3" r="1" fill="#fff"/><path d="M11 3h5l-2.5 3z" fill="var(--green)"/></svg>
      </div>
      <span class="cell plus" style="left:891px">+1:25 hrs</span>
      <span class="cell minus" style="left:975px">-31</span>
    </div>
    <div class="row">
      <span class="cell" style="left:20px">177746</span>
      <span class="cell" style="left:83px">Cedar Ridge Asphalt Plant</span>
      <span class="cell" style="left:218px">BZJV-185 from mm 77-98</span>
      <span class="cell" style="left:358px">Harlow Construction - North Division</span>
      <span class="cell" style="left:535px">Accepted</span>
      <div class="tons"><div class="track"></div><div class="meta"><span>722.57 / 1500</span><span>7:30 am - 5:00 pm</span></div></div>
      <div class="waits">
        <svg width="18" height="8"><path d="M0 8V2l3 2V2l3 2V0h2v8z" fill="#666"/><path d="M13 3l2.5 3h-5z" fill="var(--red)"/></svg>
        <svg width="22" height="8"><rect x="0" y="1" width="6" height="5" fill="#666"/><path d="M6 2.5h2.5l1.5 2V6H6z" fill="#666"/><circle cx="2" cy="7" r="1" fill="#666"/><circle cx="8" cy="7" r="1" fill="#666"/><path d="M17 3l2.5 3h-5z" fill="var(--red)"/></svg>
        <svg width="18" height="9"><path d="M3.5 0a3 3 0 0 1 3 3c0 2-3 6-3 6s-3-4-3-6a3 3 0 0 1 3-3z" fill="#666"/><circle cx="3.5" cy="3" r="1" fill="#fff"/><path d="M11 3h5l-2.5 3z" fill="var(--green)"/></svg>
      </div>
      <span class="cell plus" style="left:891px">+1:25 hrs</span>
      <span class="cell minus" style="left:975px">-31</span>
    </div>
    <div class="row">
      <span class="cell" style="left:20px">177746</span>
      <span class="cell" style="left:83px">Cedar Ridge Asphalt Plant</span>
      <span class="cell" style="left:218px">BZJV-185 from mm 77-98</span>
      <span class="cell" style="left:358px">Harlow Construction - North Division</span>
      <span class="cell" style="left:535px">Accepted</span>
      <div class="tons"><div class="track"></div><div class="meta"><span>722.57 / 1500</span><span>7:30 am - 5:00 pm</span></div></div>
      <div class="waits">
        <svg width="18" height="8"><path d="M0 8V2l3 2V2l3 2V0h2v8z" fill="#666"/><path d="M13 3l2.5 3h-5z" fill="var(--red)"/></svg>
        <svg width="22" height="8"><rect x="0" y="1" width="6" height="5" fill="#666"/><path d="M6 2.5h2.5l1.5 2V6H6z" fill="#666"/><circle cx="2" cy="7" r="1" fill="#666"/><circle cx="8" cy="7" r="1" fill="#666"/><path d="M17 3l2.5 3h-5z" fill="var(--red)"/></svg>
        <svg width="18" height="9"><path d="M3.5 0a3 3 0 0 1 3 3c0 2-3 6-3 6s-3-4-3-6a3 3 0 0 1 3-3z" fill="#666"/><circle cx="3.5" cy="3" r="1" fill="#fff"/><path d="M11 3h5l-2.5 3z" fill="var(--green)"/></svg>
      </div>
      <span class="cell plus" style="left:891px">+1:25 hrs</span>
      <span class="cell minus" style="left:975px">-31</span>
    </div>
  </div>
</section>

<article class="card" style="left:174px">
  <span class="card-close">×</span>
  <div class="card-title">Order 17746</div>
  <div class="card-sub">Avg Cycle Time : 2 hrs 27 min</div>
  <div class="card-kind"><svg width="15" height="12"><path d="M0 12V4l4 3V4l4 3V1h3v11z" fill="#999"/></svg>Plant (min)</div>
  <div class="metric" style="top:76px"><span class="lbl">Planned</span><span class="bar" style="width:121px;background:var(--blue)"></span><span class="val" style="left:180px">30</span></div>
  <div class="metric" style="top:95px"><span class="lbl">Actual</span><span class="bar" style="width:151px;background:var(--red)"></span><span class="val" style="left:209px">33</span></div>
</article>

<article class="card" style="left:431px">
  <span class="card-close">×</span>
  <div class="card-title">Order 17746</div>
  <div class="card-sub">Avg Cycle Time : 2 hrs 27 min</div>
  <div class="card-kind"><svg width="19" height="14"><rect x="0" y="1" width="11" height="9" fill="#999"/><path d="M11 4h4.5l3 4v2H11z" fill="#999"/><circle cx="4" cy="12" r="2" fill="#999" stroke="#fff"/><circle cx="15" cy="12" r="2" fill="#999" stroke="#fff"/></svg>Diving (min)</div>
  <div class="metric" style="top:76px"><span class="lbl">Planned</span><span class="bar" style="width:91px;background:var(--yellow)"></span><span class="val" style="left:151px">60</span></div>
  <div class="metric" style="top:95px"><span class="lbl">Actual</span><span class="bar" style="width:171px;background:var(--red)"></span><span class="val" style="left:223px">83</span></div>
</article>

<article class="card" style="left:686px">
  <span class="card-close">×</span>
  <div class="card-title">Order 17746</div>
  <div class="card-sub">Avg Cycle Time : 2 hrs 27 min</div>
  <div class="card-kind"><svg width="12" height="15"><path d="M6 0a6 6 0 0 1 6 6c0 4-6 9-6 9S0 10 0 6a6 6 0 0 1 6-6z" fill="#999"/><circle cx="6" cy="6" r="2.2" fill="#fff"/></svg>Jobsite (min)</div>
  <div class="metric" style="top:76px"><span class="lbl">Planned</span><span class="bar" style="width:121px;background:var(--green)"></span><span class="val" style="left:180px">30</span></div>
  <div class="metric" style="top:95px"><span class="lbl">Actual</span><span class="bar" style="width:121px;background:var(--green)"></span><span class="val" style="left:180px">30</span></div>
</article>

<article class="card" style="left:942px">
  <span class="card-close">×</span>
  <div class="card-title">Order 17746</div>
  <div class="card-sub">Avg Cycle Time : 2 hrs 27 min</div>
  <div class="card-kind"><svg width="14" height="14"><circle cx="7" cy="7" r="5" fill="#999" stroke="#999" stroke-width="3" stroke-dasharray="2.5 1.4"/><circle cx="7" cy="7" r="2" fill="#fff"/></svg>Equipment (min)</div>
  <div class="metric" style="top:76px"><span class="lbl">Planned</span><span class="bar" style="width:91px;background:var(--teal)"></span><span class="val" style="left:151px">60</span></div>
  <div class="metric" style="top:95px"><span class="lbl">Actual</span><span class="bar" style="width:157px;background:var(--red)"></span><span class="val" style="left:210px">83</span></div>
</article>
</body>
</html>
```